Trade Show booth design

I need the following designs for my trade booth:
1. backboard design 3m Wx2mH
2. Tressle table, tablecloth front panel design 1800W x 740mmH
3. Pop-up banner. I have included our logos and some design content ideas:
Headline:
"Cleaner Classrooms. Safer Schools."
Subheadline:
"Specialist Cleaning Solutions for Education Facilities"
Key Points to Grab Attention:
Healthy Environments: Create hygienic, safe learning spaces for students and staff with our expert cleaning services.
Tailored to Your Needs: Custom cleaning plans for classrooms, labs, libraries, and sports facilities.
Affordable Excellence: Premium results without premium costs – tailored plans mean you only pay for what you need.
Safety First: All staff are trained, highly vetted, and hold current Working with Children Checks (WWCC).
Eco-Conscious Cleaning: Using non-toxic, eco-friendly products certified for health and safety.
What Schools Really Need:
Reliability: Consistent, high-quality cleaning from a trusted provider.
Cost-Effectiveness: Solutions that fit tight budgets while maintaining high standards.
Expertise: Over 30 years of experience in education facility cleaning.
Disinfection Services: Focus on high-touch areas to reduce the spread of germs and ensure peace of mind.
Visual Elements:
Images of bright, clean classrooms, a happy teacher welcoming students, or students collaborating in a spotless library.
Icons representing safety (shield), hygiene (sparkling star), and eco-friendliness (leaf).
Your logo with the tagline: "Trusted by Queensland Schools Since 1995."
Call-to-Action:
"Visit us to discuss your school’s cleaning needs and book a FREE consultation."
Include contact details: Phone: 1300 648 319 | Website: www.vardenmop.com.au
Target Market(s)
Education sector
Industry/Entity Type
Commercial Cleaning
Font styles to use
Other font styles liked:
- Montserrat
Look and feel

```html
<!DOCTYPE html>
<html lang="en">
<head>
<meta charset="utf-8">
<title>Varden Mop – Education Cleaning Pop-up Banner</title>
<link href="https://fonts.googleapis.com/css2?family=Bebas+Neue&family=Poppins:wght@500;600;800&display=swap" rel="stylesheet">
<style>
  :root{
    --navy:#1b3a5f;
    --sky:#12b2e8;
    --white:#ffffff;
    --wall:#f4f2ee;
    --wood:#d9984d;
  }
  html,body{margin:0;padding:0;width:1200px;height:2199px;overflow:hidden;background:var(--white);}
  .banner{position:relative;width:1200px;height:2199px;background:var(--white);overflow:hidden;font-family:'Poppins',sans-serif;}
  .hero-art{position:absolute;left:0;top:0;width:1200px;height:1100px;}
  .brand{position:absolute;left:0;top:95px;width:1200px;display:flex;justify-content:center;align-items:center;gap:22px;}
  .brand-dot{width:34px;height:34px;border-radius:50%;background:var(--navy);}
  .brand-name{font-family:'Poppins',sans-serif;font-weight:600;font-size:84px;line-height:1;color:var(--navy);letter-spacing:2px;}
  .headline{position:absolute;left:0;top:1068px;width:1200px;text-align:center;font-family:'Bebas Neue',sans-serif;font-size:114px;line-height:118px;letter-spacing:1px;margin:0;font-weight:400;}
  .headline .line-dark{display:block;color:var(--navy);}
  .headline .line-sky{display:block;color:var(--sky);}
  .service-band{position:absolute;left:0;top:1342px;width:1200px;height:217px;background:var(--navy);color:var(--white);text-align:center;}
  .service-band .specialty{position:absolute;left:0;top:38px;width:100%;font-family:'Bebas Neue',sans-serif;font-size:68px;line-height:1;}
  .service-band .eco{position:absolute;left:0;top:114px;width:100%;font-family:'Poppins',sans-serif;font-weight:800;font-size:58px;line-height:1.1;}
  .features{position:absolute;left:0;top:1610px;width:1200px;margin:0;padding:0;list-style:none;}
  .feature{position:relative;height:136px;}
  .feature-icon{position:absolute;left:128px;top:0;width:94px;height:94px;}
  .feature-text{position:absolute;left:259px;top:8px;width:900px;font-size:31px;font-weight:500;line-height:44px;color:var(--navy);text-transform:uppercase;}
  .web-bar{position:absolute;left:0;top:2030px;width:1200px;height:100px;background:var(--sky);display:flex;justify-content:center;align-items:center;gap:20px;color:var(--white);}
  .web-bar svg{width:40px;height:40px;}
  .web-bar span{font-size:44px;font-weight:500;letter-spacing:2px;}
</style>
</head>
<body>
<div class="banner">

  <svg class="hero-art" viewBox="0 0 1200 1100" xmlns="http://www.w3.org/2000/svg">
    <defs>
      <linearGradient id="classroomTones" x1="0" y1="0" x2="0" y2="1">
        <stop offset="0" stop-color="#ffffff"/>
        <stop offset="0.28" stop-color="#ffffff"/>
        <stop offset="0.45" stop-color="#f1f0ec"/>
        <stop offset="0.62" stop-color="#c9cfc6"/>
        <stop offset="0.75" stop-color="#e0ad6c"/>
        <stop offset="1" stop-color="#d08a3e"/>
      </linearGradient>
      <clipPath id="photoCircle"><circle cx="560" cy="400" r="500"/></clipPath>
    </defs>
    <polygon points="0,0 144,0 72,70" fill="var(--sky)"/>
    <circle cx="560" cy="400" r="620" fill="var(--sky)"/>
    <rect x="0" y="0" width="1200" height="1100" clip-path="url(#photoCircle)" fill="url(#classroomTones)" role="img" aria-label="Bright, clean classroom with chalkboard, windows and rows of wooden desks"/>
    <path d="M1080 873 q4 18 22 22 q-18 4 -22 22 q-4 -18 -22 -22 q18 -4 22 -22z" fill="var(--sky)"/>
    <path d="M996 950 q7 37 44 44 q-37 7 -44 44 q-7 -37 -44 -44 q37 -7 44 -44z" fill="var(--sky)"/>
  </svg>

  <div class="brand">
    <div class="brand-dot"></div>
    <div class="brand-name">VARDEN MOP</div>
  </div>

  <h1 class="headline">
    <span class="line-dark">Creating Cleaner, Safer</span>
    <span class="line-sky">Learning Environments</span>
  </h1>

  <div class="service-band">
    <div class="specialty">Specialists in Education Facility Cleaning</div>
    <div class="eco">&amp; ECO FRIENDLY SERVICES</div>
  </div>

  <ul class="features">
    <li class="feature">
      <svg class="feature-icon" viewBox="0 0 94 94">
        <circle cx="47" cy="47" r="45" fill="var(--sky)"/>
        <circle cx="47" cy="47" r="30" fill="none" stroke="var(--white)" stroke-width="5"/>
        <path d="M33 48 l10 10 l19 -21" fill="none" stroke="var(--white)" stroke-width="7" stroke-linecap="round" stroke-linejoin="round"/>
      </svg>
      <div class="feature-text">Over 30 years of expertise in commercial<br>cleaning</div>
    </li>
    <li class="feature">
      <svg class="feature-icon" viewBox="0 0 94 94">
        <circle cx="47" cy="47" r="45" fill="var(--sky)"/>
        <path d="M20 44 l14 -10 l14 8 l14 -8 l14 10" fill="none" stroke="var(--white)" stroke-width="5" stroke-linecap="round" stroke-linejoin="round"/>
        <path d="M30 48 l16 14 q4 3 8 0 l12 -12" fill="none" stroke="var(--white)" stroke-width="5" stroke-linecap="round" stroke-linejoin="round"/>
      </svg>
      <div class="feature-text">Trusted by schools, universities, and TAFEs<br>across Queensland</div>
    </li>
    <li class="feature">
      <svg class="feature-icon" viewBox="0 0 94 94">
        <circle cx="47" cy="47" r="45" fill="var(--sky)"/>
        <path d="M47 66 C30 60 26 42 30 26 C44 32 50 46 47 66z" fill="var(--white)"/>
        <path d="M47 66 C64 60 68 42 64 26 C50 32 44 46 47 66z" fill="var(--white)" opacity="0.85"/>
      </svg>
      <div class="feature-text">100% carbon neutral and eco-certified<br>services.</div>
    </li>
  </ul>

  <div class="web-bar">
    <svg viewBox="0 0 40 40" fill="none" stroke="var(--white)" stroke-width="2.6">
      <circle cx="20" cy="20" r="17"/>
      <ellipse cx="20" cy="20" rx="7.5" ry="17"/>
      <line x1="3" y1="20" x2="37" y2="20"/>
      <path d="M6 11 h28 M6 29 h28"/>
    </svg>
    <span>www.vardenmop.com.au</span>
  </div>

</div>
</body>
</html>
```